Flyer für ambulanten Pflegedienst
Zielgruppe
Ambulanter Pflegedienst, Potentielle Kunden für Grund- und Behandlungspflege, nicht nur Pflegebedürftige, sondern auch Angehörige. Flyer dient zur Auslage, beispielsweise in Wartezimmern von Ärzten.
Aufgabenstellung
Ausführliches Briefing mit Aufbau und Text in der Anlage, ebenso das Bildmaterial, Fonts, Logos. Flyer in A4 Wickelfalz, bitte die Gestaltungsvorlage mit den Maßen des Druckanbieters (ebenfalls anbei) beachten. Vorerst hauptsächlich KI-generierte/Stockfotos vorhanden, Fotoshooting folgt im Juli und Bilder werden dann ggf. nochmal ersetzt um persönliche Ebene zu erzeugen. Der erste Wurf muss aber vorerst so erfolgen. Übergabe der Daten: Druckfähiges PDF, PDF mit Ebenen und AI

```html
<!DOCTYPE html>
<html lang="de">
<head>
<meta charset="utf-8">
<title>Lindner Hauskrankenpflege – Flyer Wickelfalz</title>
<link href="https://fonts.googleapis.com/css2?family=Montserrat:wght@400;500;600;700&family=Outfit:wght@400;500;600;700&display=swap" rel="stylesheet">
<style>
:root{
  --navy:#1f3f8e;
  --navy-dark:#1a3478;
  --green:#3b8b3a;
  --green-soft:#d7e8d3;
  --ink:#5a5a5a;
  --lavender:#e6e7f2;
  --line:#9a9a9a;
  --white:#ffffff;
}
*{box-sizing:border-box;margin:0;padding:0}
html,body{width:1200px;height:4000px;overflow:hidden;background:var(--white)}
body{font-family:'Montserrat',sans-serif;color:var(--ink);position:relative}
h1,h2,h3,h4,.head{font-family:'Outfit',sans-serif}
b{font-weight:700;color:#333}

.brand-header{position:absolute;top:70px;right:90px;display:flex;align-items:center;gap:22px}
.brand-header .name{font-family:'Montserrat',sans-serif;font-weight:600;font-size:62px;color:var(--navy);line-height:1}
.brand-header .dot{width:34px;height:34px;border-radius:50%;background:var(--navy)}

.spread{position:absolute;left:50px;width:1100px;height:776px;border:1px solid var(--line);display:flex;background:var(--white)}
.spread.outside{top:420px}
.spread.inside{top:1380px}
.panel{position:relative;height:100%}
.outside .panel{width:366.67px}

.photo{border-radius:14px}

/* outside left */
.p-about{padding:42px 30px 30px 30px}
.p-about h2{color:var(--navy);font-size:25px;font-weight:600;line-height:1.2;margin-bottom:14px}
.p-about p{font-size:14px;line-height:1.35;margin-bottom:36px}
.p-about h3{color:var(--navy);font-size:22px;font-weight:600;margin-bottom:12px}
.contact{position:absolute;left:30px;right:20px;bottom:36px;font-size:14px;line-height:1.35;color:var(--navy)}
.contact .hours{margin-bottom:22px;font-weight:600}
.contact strong{font-weight:700}

/* outside middle */
.p-house{border-left:1px solid #eee;background:linear-gradient(90deg,#eef5ec 0 16%,#fff 16%)}
.vertical{position:absolute;writing-mode:vertical-rl;transform:rotate(180deg);font-family:'Outfit',sans-serif;font-weight:700;white-space:nowrap}
.p-house .vertical{left:4px;bottom:36px;font-size:40px;color:var(--green-soft)}
.sub-brand{position:absolute;top:38px;left:66px;display:flex;align-items:center;gap:10px}
.sub-brand .name{font-size:20px;font-weight:600;color:var(--green)}
.sub-brand .dot{width:16px;height:16px;border-radius:50%;background:var(--green)}
.p-house .photo{position:absolute;top:60px;right:24px;width:262px;height:212px;background:linear-gradient(135deg,#dfe9dd,#b9cfb4 55%,#e8ecef)}
.house-body{position:absolute;top:300px;left:82px;right:20px;font-size:14px;line-height:1.3}
.house-body h2{color:var(--green);font-size:23px;font-weight:600;line-height:1.2;margin-bottom:8px}
.house-body h4{color:var(--green);font-size:17px;font-weight:600;margin-bottom:2px}
.house-body .svc{position:relative;margin-bottom:20px}
.house-body .svc.icon{padding-left:0}
.green-contact{position:absolute;left:82px;right:14px;bottom:36px;font-size:14px;line-height:1.35;color:var(--green)}
.green-contact .hours{margin-bottom:22px;font-weight:500}
.green-contact strong{font-weight:700}

/* outside right (cover) */
.p-cover .photo{position:absolute;top:0;left:0;width:100%;height:466px;border-radius:0;background:linear-gradient(160deg,#c9b59f,#e8e2da 45%,#3d5ea8 85%)}
.cover-brand{position:absolute;top:44px;right:22px;display:flex;align-items:center;gap:8px;background:rgba(255,255,255,.85);padding:6px 10px;border-radius:20px}
.cover-brand .name{font-size:16px;font-weight:600;color:var(--navy)}
.cover-brand .dot{width:12px;height:12px;border-radius:50%;background:var(--navy)}
.cover-band{position:absolute;top:366px;left:0;width:100%;height:100px;background:rgba(31,63,142,.92);color:#fff;font-family:'Outfit',sans-serif;font-size:25px;line-height:1.12;padding:12px 60px 0 58px}
.cover-body{position:absolute;top:490px;left:56px;right:24px}
.cover-body h2{color:var(--navy);font-size:22px;font-weight:600;line-height:1.2;margin-bottom:6px}
.cover-body p{font-size:13px;line-height:1.35}
.pills{position:absolute;top:630px;left:10px;display:flex;flex-direction:column;gap:10px}
.pill{width:230px;height:21px;border-radius:5px;background:var(--navy);color:#fff;font-size:13px;font-weight:600;text-align:center;line-height:21px}
.tick{position:absolute;top:640px;right:28px}

/* inside left */
.p-who{width:366.67px;padding-top:46px}
.banner{margin-left:0;width:318px;background:var(--navy);color:#fff;font-family:'Outfit',sans-serif;font-size:23px;line-height:1.15;padding:8px 0 8px 56px;border-radius:0 8px 8px 0}
.who-body{padding:18px 24px 0 56px;font-size:14px;line-height:1.3}
.who-body p{margin-bottom:14px}
.p-who .photo{position:absolute;left:54px;top:412px;width:262px;height:214px;background:linear-gradient(135deg,#3a5aa5,#cfd3de 55%,#2d4a92)}
.p-who .vertical{left:8px;bottom:40px;font-size:40px;color:#dde3f0}
.quote{position:absolute;left:62px;top:648px;width:220px;font-size:13px;font-weight:600;color:var(--navy);line-height:1.25}
.quote-mark{position:absolute;left:230px;top:690px;font-family:'Outfit',sans-serif;font-size:90px;line-height:1;color:#d7dcea}

/* inside right */
.p-services{width:733.33px;background:var(--lavender);border-left:1px solid #ddd}
.p-services .vertical{left:8px;bottom:36px;font-size:42px;color:var(--white)}
.svc-intro{position:absolute;top:56px;left:70px;width:330px}
.svc-intro h2{color:var(--navy);font-size:28px;font-weight:600;line-height:1.15;margin-bottom:10px}
.svc-intro p{font-size:14px;line-height:1.3}
.p-services .photo{position:absolute;top:46px;right:34px;width:286px;height:234px;background:linear-gradient(135deg,#2f4e98,#d9d4cc 55%,#efece6)}
.svc-list{position:absolute;list-style:none}
.svc-list.left{top:228px;left:70px;width:300px}
.svc-list.right{top:316px;left:390px;width:312px}
.svc-list li{display:flex;gap:12px;margin-bottom:22px;font-size:13.5px;line-height:1.28}
.svc-list .ico{flex:0 0 48px;height:48px;border-radius:50%;background:#b5c3e3}
.svc-list h4{color:var(--navy);font-size:18px;font-weight:600;line-height:1.1;margin-bottom:2px}

.fonts-note{position:absolute;top:2240px;left:128px;font-family:'Outfit',sans-serif;color:#555;font-size:52px;line-height:1.2}
.fonts-note h2{font-weight:700;font-size:52px}
.fonts-note p{font-weight:500}
</style>
</head>
<body>

<header class="brand-header">
  <span class="name">Lindner Hauskrankenpflege</span>
  <span class="dot"></span>
</header>

<!-- Außenseite -->
<section class="spread outside">
  <div class="panel p-about">
    <h2>Pflege braucht Vertrauen.<br>Und Menschen,<br>die da sind.</h2>
    <p>Gute Pflege entsteht durch <b>Aufmerksamkeit, Erfahrung</b> und <b>ein verlässliches Team.</b> Bei der Hauskrankenpflege Lindner arbeiten engagierte Pflegekräfte, Betreuungskräfte und Fachpersonen Hand in Hand – <b>mit Herz, Respekt und fachlicher Kompetenz.</b> Über 40 Mitarbeitende geben Tag für Tag ihr Bestes für Sie und Ihre Angehörigen.</p>
    <h3>Wir sind für Sie da.</h3>
    <p>Sie möchten sich informieren oder ein persönliches Gespräch vereinbaren? Wir beraten Sie gerne – <b>unkompliziert, persönlich und unverbindlich.</b></p>
    <div class="contact">
      <div class="hours">Bürozeiten:<br>Mo., Di., Mi., Fr. 9 bis 12 Uhr<br>und Do. 15 bis 17 Uhr</div>
      <div><strong>Hauskrankenpflege Lindner</strong><br>Am Mühlenbach 4 · 31000 Musterstadt<br>Telefon: 0 12 34 - 56 78 0<br>info@lindner-pflege.example<br>www.lindner-pflege.example</div>
    </div>
  </div>

  <div class="panel p-house">
    <span class="vertical">Hauswirtschaftliche Versorgung</span>
    <div class="sub-brand"><span class="name">Lindner Hausdienste</span><span class="dot"></span></div>
    <div class="photo" role="img" aria-label="Foto: lächelnde Haushaltshilfe mit Reinigungswagen"></div>
    <div class="house-body">
      <h2>Hilfe im Haushalt.<br>Entlastung im Alltag.</h2>
      <div class="svc"><h4>Hilfe im Haushalt</h4>Unterstützung bei alltäglichen Aufgaben – von der <b>Grundreinigung</b> bis zur <b>Wäschepflege.</b></div>
      <div class="svc"><h4>Alltagsbegleitung &amp; Betreuung</h4>Niemand ist gern allein und <b>wir sind für Sie da,</b> wenn Sie Gesellschaft wünschen.</div>
    </div>
    <div class="green-contact">
      <div class="hours">Bürozeiten:<br>Mo., Di., Do., Fr. 8 bis 11 Uhr</div>
      <div><strong>Lindner Hausdienste GmbH</strong><br>Am Mühlenbach 4 · 31000 Musterstadt<br>Telefon: 0 12 34 - 98 76 543<br>info@lindner-hausdienste.example<br>www.lindner-hausdienste.example</div>
    </div>
  </div>

  <div class="panel p-cover">
    <div class="photo" role="img" aria-label="Foto: lächelnde Pflegekraft in blauer Dienstkleidung bei einer älteren Dame"></div>
    <div class="cover-brand"><span class="name">Lindner Hauskrankenpflege</span><span class="dot"></span></div>
    <div class="cover-band">Weil das eigene<br>Zuhause<br>Lebensqualität ist.</div>
    <div class="cover-body">
      <h2>Ihr ambulanter Pflege-<br>dienst für die Region.</h2>
      <p>Seit <b>über 30 Jahren</b> begleiten wir Menschen im <b>Raum Musterstadt und Umland</b> in ihrem vertrauten Zuhause.</p>
    </div>
    <div class="pills">
      <span class="pill">Individuelle Beratung</span>
      <span class="pill">Verlässliche Versorgung</span>
      <span class="pill">MD-geprüfte Qualität</span>
    </div>
    <svg class="tick" width="74" height="54" viewBox="0 0 74 54" aria-hidden="true">
      <ellipse cx="37" cy="27" rx="34" ry="24" fill="none" stroke="#c9cfe0" stroke-width="4"/>
      <path d="M22 27 L33 38 L58 10" fill="none" stroke="#c9cfe0" stroke-width="5" stroke-linecap="round" stroke-linejoin="round"/>
    </svg>
  </div>
</section>

<!-- Innenseite -->
<section class="spread inside">
  <div class="panel p-who">
    <h2 class="banner">Vertrauen beginnt<br>mit Zuhören.</h2>
    <div class="who-body">
      <p>Pflege bedeutet für uns mehr als Versorgung. Es geht um Menschen, ihre Gewohnheiten, ihre Wünsche und <b>das gute Gefühl, in den eigenen vier Wänden bleiben zu können.</b></p>
      <p>Deshalb nehmen wir uns Zeit für persönliche Gespräche und individuelle Lösungen. Gemeinsam mit unseren Kundinnen, Kunden und Angehörigen gestalten wir eine <b>Unterstützung, die zum Leben passt</b> – nicht umgekehrt.</p>
    </div>
    <div class="photo" role="img" aria-label="Foto: zwei Pflegekräfte begleiten eine ältere Dame"></div>
    <span class="vertical">Wer wir sind</span>
    <p class="quote">Unsere Pflege orientiert sich am Befinden der Menschen – nicht am Befund.</p>
    <span class="quote-mark" aria-hidden="true">“</span>
  </div>

  <div class="panel p-services">
    <span class="vertical">Unsere Leistungen</span>
    <div class="svc-intro">
      <h2>Unterstützung, die den Alltag leichter macht.</h2>
      <p>Jeder Mensch braucht etwas anderes. Deshalb richten wir unsere Leistungen individuell nach Ihrer <b>persönlichen Situation</b> aus.</p>
    </div>
    <div class="photo" role="img" aria-label="Foto: Pflegekraft hilft einer älteren Dame am Arm"></div>
    <ul class="svc-list left">
      <li><span class="ico"></span><div><h4>Grundpflege</h4>Unterstützung bei <b>Körperpflege, Mobilität, Ernährung</b> und allem, was <b>Sicherheit im Alltag</b> gibt.</div></li>
      <li><span class="ico"></span><div><h4>Behandlungspflege</h4><b>Medizinische Versorgung</b> nach ärztlicher Verordnung – zum Beispiel <b>Wundversorgung, Medikamentengabe</b> oder <b>Injektionen.</b></div></li>
      <li><span class="ico"></span><div><h4>Betreuung &amp; Alltagsbegleitung</h4>Begleitung im Alltag, stundenweise Betreuung, <b>Unterstützung bei Demenz</b> sowie Entlastung für Angehörige.</div></li>
      <li><span class="ico"></span><div><h4>Verhinderungspflege</h4><b>Auszeiten</b> im Rahmen der Verhinderungspflege, denn auch <b>pflegende Angehörige</b> müssen mal durchatmen.</div></li>
    </ul>
    <ul class="svc-list right">
      <li><span class="ico"></span><div><h4>Beratung</h4>Pflegeberatung nach § 37.3 SGB XI zur <b>Sicherstellung des Pflegegeld-Bezugs,</b> Unterstützung bei Anträgen und Hilfe bei allen Fragen rund um Pflegeleistungen.</div></li>
      <li><span class="ico"></span><div><h4>Hausnotruf &amp; Erreichbarkeit</h4>Sicherheit rund um die <b>Uhr</b> – mit einem Team, das erreichbar bleibt.</div></li>
      <li><span class="ico"></span><div><h4>Palliative Versorgung</h4>Als spezialisierter Anbieter ist uns die Versorgung und Begleitung zum Ende des Lebens ein <b>besonderes Herzensanliegen.</b></div></li>
    </ul>
  </div>
</section>

<section class="fonts-note">
  <h2>Verwendete Schriften:</h2>
  <p>Headlines - Ornitons</p>
  <p>Fließtext - Montserrat</p>
</section>

</body>
</html>
```